1 page marketing brochure for subcontractor services for Florida's Petroleum Contamination cleanup

I need a marketing brochure that can be emailed to potential clients to offer our comprehensive service capabilities to Agency Term Contractors in the Coastal Bureau of Habitat Stewardship's (CBHS) Fuel Recovery Initiative. We offer turnkey support from project management, monitoring, reporting, soil and groundwater assessment, remediation system engineering, design, construction, and system rental. We would like to see designs that use the green and goldish colors in our logo. I have attached the icon from our logo and an amateur in-house created design with some key points that are important to us. The icons used as bullet points can change. I've added examples of industry correct drilling icons. I also added a second picture of a system trailer in use. We are open to different Fonts and are open to assistance with copy refinement. This single page flyer is intended only for digital use (email/website) at this time.
Updates

Target Market(s)

Agency Term contractors in Coastal Bureau of Habitat Stewardship Fuel Recovery Initiative

Industry/Entity Type

Petroleum cleanup in Florida

Requirements
Should not have
• Don't show the Varnel name in the photo. See attached examples of industry appropriate drilling icons

```html
<!DOCTYPE html>
<html lang="en">
<head>
<meta charset="utf-8">
<title>Meridane Corporation – Fuel Recovery Initiative Services</title>
<link href="https://fonts.googleapis.com/css2?family=Inter:wght@400;500;600;700&display=swap" rel="stylesheet">
<style>
  :root {
    --green-deep: #2f5a3f;
    --green-panel: #325c41;
    --green-soft: #6f9a5e;
    --gold: #c9a56a;
    --gold-line: #cfae76;
    --cream: #f1e6d2;
    --cream-text: #f1e8d6;
    --text-green: #2c5239;
  }
  * { margin: 0; padding: 0; box-sizing: border-box; }
  html, body { width: 1200px; height: 1200px; overflow: hidden; background: var(--cream); }
  body { font-family: "Inter", Arial, sans-serif; }
  .flyer { position: relative; width: 1200px; height: 1200px; overflow: hidden; }
  .backdrop { position: absolute; inset: 0; }

  .brand { position: absolute; left: 80px; top: 98px; display: flex; align-items: center; gap: 22px; }
  .brand-mark { width: 122px; height: 122px; border-radius: 50%; background: var(--green-deep); flex: none; }
  .brand-name { font-size: 45px; font-weight: 600; line-height: 1.08; color: var(--text-green); letter-spacing: -0.3px; }

  .rule { position: absolute; height: 2px; background: var(--gold-line); }
  .rule-left-top { left: 80px; top: 305px; width: 440px; }
  .rule-left-bottom { left: 80px; top: 546px; width: 440px; }
  .rule-right { left: 676px; top: 337px; width: 432px; }

  .program-title { position: absolute; left: 80px; top: 337px; width: 470px;
    font-size: 30px; font-weight: 600; line-height: 44px; color: var(--text-green); }

  .services { list-style: none; }
  .services li { position: absolute; left: 78px; width: 470px; display: flex; align-items: flex-start; gap: 30px; }
  .services li:nth-child(1) { top: 585px; }
  .services li:nth-child(2) { top: 657px; }
  .services li:nth-child(3) { top: 731px; }
  .services li:nth-child(4) { top: 804px; }
  .services li:nth-child(5) { top: 881px; }
  .services li:nth-child(6) { top: 994px; }
  .services svg { width: 50px; height: 54px; flex: none; stroke: var(--gold); fill: none; stroke-width: 2.2; stroke-linecap: round; stroke-linejoin: round; }
  .services p { font-size: 21px; line-height: 30px; color: var(--text-green); white-space: nowrap; }
  .services p.strong { font-weight: 600; }

  .headline { position: absolute; left: 676px; top: 98px; width: 500px;
    font-size: 45px; font-weight: 700; line-height: 1.22; color: var(--cream-text); }
  .capabilities { position: absolute; left: 676px; top: 355px; width: 520px;
    font-size: 21px; line-height: 35px; color: var(--cream-text); white-space: nowrap; }
</style>
</head>
<body>
<main class="flyer">
  <svg class="backdrop" viewBox="0 0 1200 1200" width="1200" height="1200">
    <defs>
      <linearGradient id="site-photo" x1="0" y1="0" x2="0" y2="1">
        <stop offset="0" stop-color="#3f6aa8"/>
        <stop offset="0.45" stop-color="#7f9fc7"/>
        <stop offset="0.6" stop-color="#4d5f3c"/>
        <stop offset="0.75" stop-color="#b49a6c"/>
        <stop offset="1" stop-color="#e6e6e2"/>
      </linearGradient>
    </defs>
    <rect x="0" y="0" width="1200" height="1200" fill="#f1e6d2"/>
    <rect x="600" y="0" width="600" height="1200" fill="#325c41"/>
    <path d="M600 820 C680 640 790 650 880 660 C1000 660 1130 580 1200 470 L1200 1200 L600 1200 Z" fill="#6f9a5e"/>
    <path d="M600 840 C680 670 790 670 880 678 C1000 678 1130 600 1200 500 L1200 1200 L600 1200 Z" fill="#c9a56a"/>
    <path role="img" aria-label="Photo of a green remediation system trailer parked on a gravel site with trees and blue sky"
      d="M600 860 C680 690 790 690 880 696 C1000 696 1130 620 1200 525 L1200 1150 L600 1150 Z" fill="url(#site-photo)"/>
    <path d="M0 990 C60 1090 160 1135 300 1130 C450 1125 560 1085 720 1080 C900 1075 1050 1130 1200 1160 L1200 1200 L0 1200 Z" fill="#c9a56a"/>
    <path d="M0 1018 C60 1112 160 1155 300 1150 C450 1145 560 1108 720 1103 C900 1098 1050 1150 1200 1178 L1200 1200 L0 1200 Z" fill="#6f9a5e"/>
    <path d="M0 1046 C60 1135 160 1175 300 1170 C450 1165 560 1130 720 1126 C900 1122 1050 1170 1200 1195 L1200 1200 L0 1200 Z" fill="#2f5a3f"/>
  </svg>

  <div class="brand">
    <span class="brand-mark"></span>
    <span class="brand-name">Meridane<br>Corporation</span>
  </div>

  <div class="rule rule-left-top"></div>
  <h2 class="program-title">Turnkey Service for Contractors, Coastal Bureau of Habitat Stewardship Fuel Recovery Initiative</h2>
  <div class="rule rule-left-bottom"></div>

  <ul class="services">
    <li>
      <svg viewBox="0 0 50 54"><path d="M6 52V10h14v42M20 14h22v8H20M30 22v30M14 52V36h8"/></svg>
      <p>Project management, monitoring,<br>reporting and site oversight,</p>
    </li>
    <li>
      <svg viewBox="0 0 50 54"><circle cx="34" cy="14" r="9"/><path d="M4 34c0-8 6-12 14-12h10M4 34v10c0 4 3 6 6 6h30c3 0 6-3 6-6v-6H18"/></svg>
      <p class="strong">Soil and groundwater<br>Assessment and Water</p>
    </li>
    <li>
      <svg viewBox="0 0 50 54"><path d="M22 4v30M28 4v22h-6M10 44h30l-4-10H14zM6 52h38"/></svg>
      <p class="strong">Remediation system engineering<br>and design services,</p>
    </li>
    <li>
      <svg viewBox="0 0 50 54"><rect x="4" y="6" width="40" height="44" rx="2"/><path d="M16 6v44M16 22h20a8 8 0 0 1 0 16H28"/></svg>
      <p class="strong">Construction and site<br>Services.</p>
    </li>
    <li>
      <svg viewBox="0 0 50 54"><circle cx="12" cy="8" r="5"/><path d="M12 13v26M12 24h22M34 24v14"/><circle cx="36" cy="44" r="7"/><path d="M6 52h36"/></svg>
      <p>A. Full system and equipment<br>Assessment, monitoring, restoration<br>Reporting for every property</p>
    </li>
    <li>
      <svg viewBox="0 0 50 54"><rect x="4" y="12" width="42" height="38" rx="2"/><path d="M16 12V6h18v6"/><rect x="12" y="22" width="26" height="18" rx="3"/></svg>
      <p>A. Rental remediation systems for<br>Prime contractors, ready to use,<br>delivered, set up and faster</p>
    </li>
  </ul>

  <h1 class="headline">Comprehensive Service Support for Fuel Recovery Contractors,</h1>
  <div class="rule rule-right"></div>
  <p class="capabilities">
    To Turnkey Support for<br>
    Prime Contractors, from Project Management,<br>
    Monitoring, Reporting and Assessment,<br>
    Soil and Groundwater Assessment,<br>
    Remediation Engineering, System<br>
    Design, Construction, Soil,<br>
    System Rental
  </p>
</main>
</body>
</html>
```